Driver License Monitoring Application Marketing Website

We need a new web design for our web application. The product is called "PermitPulseNow." We provide a driver license monitoring service to companies and local government bodies with driver fleets. Our current website is available at www.permitpulsenow.example.

I prefer a clean, single-page design with good SEO. Attached are some PDFs with data about the project.

Target Market(s)

Companies with driver fleets, local government.

Industry/Entity Type

Government

Coding

Coded - Design and coding required

Number of Pages Required

1 page

Colors
000000

Requirements
Must have
• Content from current www.permitpulsenow.example and attached PDFs.
Nice to have
• Prefer a simple Bootstrap or similar design for easy editing.
• Room for a simple video explanation of how the product works (we don't have an actual video yet)

```html
<!DOCTYPE html>
<html lang="en">
<head>
<meta charset="utf-8">
<title>PermitPulseNow — Driver License Monitoring</title>
<link href="https://fonts.googleapis.com/css2?family=Maven+Pro:wght@400;500&family=Open+Sans:wght@600;700&display=swap" rel="stylesheet">
<style>
  :root {
    --topbar-bg: #1b1b1b;
    --nav-bg: #161616;
    --divider: #2a2a2a;
    --accent: #c9282d;
    --text-light: #ffffff;
    --logo-ink: #8a8a8a;
    --sky: #9fc6e6;
    --sea: #4f7fae;
    --hill: #8a6a45;
    --road: #6e6a66;
  }
  * { margin: 0; padding: 0; box-sizing: border-box; }
  html, body { width: 1200px; height: 774px; overflow: hidden; background: var(--nav-bg); }
  .page { position: relative; width: 1200px; height: 774px; font-family: "Maven Pro", sans-serif; }

  .top-bar {
    position: absolute; left: 0; top: 0; width: 1200px; height: 55px;
    background: var(--topbar-bg); border-bottom: 1px solid var(--divider);
  }
  .top-bar .search { position: absolute; left: 97px; top: 18px; width: 19px; height: 19px; }

  .main-nav {
    position: absolute; left: 0; top: 55px; width: 1200px; height: 108px;
    background: var(--nav-bg);
  }
  .brand {
    position: absolute; left: 45px; top: 40px;
    font-family: "Maven Pro", sans-serif; font-weight: 500; font-size: 22px;
    color: var(--logo-ink); letter-spacing: 0.5px;
  }
  .menu { position: absolute; top: 34px; left: 0; width: 1200px; list-style: none; }
  .menu li {
    position: absolute; top: 0; height: 40px; line-height: 40px;
    color: var(--text-light); font-size: 17px; white-space: nowrap;
  }
  .menu li.active { background: var(--accent); border-radius: 2px; padding: 0 14px; }
  .menu .caret { display: inline-block; width: 10px; height: 7px; margin-left: 4px; vertical-align: middle; }

  .hero { position: absolute; left: 0; top: 163px; width: 1200px; height: 611px; overflow: hidden; }
  .hero-photo {
    position: absolute; inset: 0;
    background:
      linear-gradient(160deg, rgba(255,255,255,0.35) 0%, rgba(255,255,255,0) 30%),
      linear-gradient(180deg, var(--sky) 0%, #cfe2f1 22%, var(--sea) 32%, #3c6a94 50%, var(--hill) 68%, var(--road) 100%);
  }
  .hero-copy { position: absolute; left: 76px; top: 346px; color: var(--text-light); font-family: "Open Sans", sans-serif; }
  .hero-title { font-weight: 600; font-size: 43px; line-height: 47px; width: 500px; }
  .hero-sub { margin-top: 26px; font-weight: 700; font-size: 21px; line-height: 25px; width: 490px; }

  .slide-arrow {
    position: absolute; top: 410px; width: 46px; height: 47px;
    background: var(--accent); border-radius: 3px;
  }
  .slide-arrow svg { position: absolute; left: 17px; top: 16px; }
  .slide-arrow.prev { left: 12px; }
  .slide-arrow.next { left: 1138px; }
</style>
</head>
<body>
<div class="page">
  <header class="top-bar">
    <svg class="search" viewBox="0 0 20 20" aria-label="Search">
      <circle cx="8" cy="8" r="5.5" fill="none" stroke="#fff" stroke-width="3"/>
      <line x1="12" y1="12" x2="17.5" y2="17.5" stroke="#fff" stroke-width="3.2" stroke-linecap="round"/>
    </svg>
  </header>

  <nav class="main-nav">
    <div class="brand">PermitPulseNow</div>
    <ul class="menu">
      <li class="active" style="left:484px;">Home</li>
      <li style="left:585px;">About Us</li>
      <li style="left:696px;">Services</li>
      <li style="left:799px;">Portfolio</li>
      <li style="left:908px;">Pages<svg class="caret" viewBox="0 0 10 7"><polyline points="1,1 5,5 9,1" fill="none" stroke="#fff" stroke-width="2"/></svg></li>
      <li style="left:1009px;">Blog</li>
      <li style="left:1083px;">Contact</li>
    </ul>
  </nav>

  <section class="hero">
    <div class="hero-photo" role="img" aria-label="Photo of a white truck driving along a winding coastal road above the sea"></div>
    <div class="hero-copy">
      <h1 class="hero-title">Lorem ipsum dolor sit amet consectetur adipisicing elit</h1>
      <p class="hero-sub">Accusantium doloremque laudantium totam rem aperiam, eaque ipsa</p>
    </div>
    <div class="slide-arrow prev">
      <svg width="12" height="15" viewBox="0 0 12 15"><polyline points="9,2 3,7.5 9,13" fill="none" stroke="#fff" stroke-width="3"/></svg>
    </div>
    <div class="slide-arrow next">
      <svg width="12" height="15" viewBox="0 0 12 15"><polyline points="3,2 9,7.5 3,13" fill="none" stroke="#fff" stroke-width="3"/></svg>
    </div>
  </section>
</div>
</body>
</html>
```